New IPv6 service needs a Web Design

We're launching a brand new service which is designed to connect the current Internet Protocol (IPv4) to the new Internet Protocol (IPv6).
The logo can be found at http://www.brelvo-link.example
We're looking for a clean and simple design, nothing super-fancy. There has to be room for some menu items and a place where people can login (so an e-mail and password box and login button, which must be replaced by the username and a logout button when the user is logged in).
We need a place for a rotating billboard (see http://qa.zx for an example) or a video.
Designs that incorporate IPv4 - IPv6 elements (images with interconnecting networks, videos doing the same) will be rated higher, although the basic design is still the primary concern.
We need :
- A main page, with the rotating billboard and some other typical main page stuff
- 2 subpages with different formatted content blocks (1 column and 2 column)
This is a very short design contest, since we intend to go live very soon. Decision will be made quickly.
PSD file is sufficient, but it must be easy to slice to HTML/CSS (but we'll do that part ourselves).
Target Market(s)
IT Professionals
Industry/Entity Type
Internet
Look and feel
Each slider illustrates characteristics of the customer's brand and the style your logo design should communicate.

```html
<!DOCTYPE html>
<html lang="en">
<head>
<meta charset="utf-8">
<title>Brelvo – Interconnecting Networks</title>
<link href="https://fonts.googleapis.com/css2?family=Source+Sans+3:wght@400;600;700&family=PT+Sans+Narrow:wght@400;700&display=swap" rel="stylesheet">
<style>
:root{
  --blue:#1a6fb0;
  --blue-dark:#1d5f9c;
  --red:#d42a2c;
  --text:#333;
  --muted:#666;
  --header-bg:#f3f3f3;
  --footer-bg:#efefef;
  --line:#d8d8d8;
  --orange:#f39a10;
  --panel:#e6f0f8;
}
*{box-sizing:border-box;margin:0;padding:0}
html,body{width:910px;height:1200px;overflow:hidden;background:#fff}
body{position:relative;font-family:"Source Sans 3",sans-serif;color:var(--text);font-size:10px}
.abs{position:absolute}
a{color:inherit;text-decoration:none}

/* header */
.site-header{position:absolute;left:0;top:0;width:910px;height:124px;background:linear-gradient(#f7f7f7,#ececec);border-top:5px solid #e2e2e2}
.brand{position:absolute;left:31px;top:48px;display:flex;align-items:center;gap:8px;font-size:34px;font-weight:700;color:var(--blue-dark);letter-spacing:-0.5px}
.brand-dot{width:14px;height:14px;border-radius:50%;background:var(--blue)}
.login{position:absolute;top:18px;left:395px;display:flex;align-items:center;font-size:11px;color:#666}
.login input{width:90px;height:14px;border:1px solid #cfcfcf;border-radius:3px;background:#fff;margin:0 14px 0 6px}
.btn-login{background:var(--blue);color:#fff;border-radius:3px;padding:2px 13px;font-size:10px}
.welcome-user{margin-left:12px;background:#e4e4e4;padding:4px 9px;font-size:10px;color:#555}
.main-nav{position:absolute;left:398px;top:87px;display:flex;align-items:center;font-size:13px;color:#666}
.main-nav a{padding:0 19px;line-height:28px;border-left:1px dotted #aaa}
.main-nav a:nth-child(2),.main-nav a:first-child{border-left:none}
.main-nav a.active{background:var(--blue);color:#fff;border-radius:14px;padding:0 18px;margin-right:4px}

/* hero */
.hero{position:absolute;left:0;top:124px;width:910px;height:310px;background:#fff}
.hero h1{position:absolute;left:44px;top:60px;font-weight:400;font-size:29px;color:var(--blue)}
.hero h1 span{color:var(--red)}
.hero h2{position:absolute;left:46px;top:97px;font-weight:400;font-size:16px;color:#222}
.hero p{position:absolute;left:46px;top:122px;width:360px;font-size:11.6px;line-height:17px;color:var(--blue)}
.btn-more{position:absolute;left:49px;top:202px;background:var(--red);color:#fff;font-size:12px;padding:8px 16px;border-radius:2px}
.dots{position:absolute;left:51px;top:249px;display:flex;gap:4px}
.dots i{width:7px;height:7px;border-radius:50%;background:var(--blue);display:block}
.hero-art{position:absolute;left:453px;top:23px;width:387px;height:287px;background:radial-gradient(circle at 50% 45%,#6fb4ea 0,#2f86cc 22%,#e9f1f7 48%,#f6f8fa 75%)}
.hero-shadow{position:absolute;left:0;top:434px;width:910px;height:10px;background:linear-gradient(#e6eef5,#fff)}

/* content */
.section-title{font-family:"PT Sans Narrow",sans-serif;font-size:17px;color:var(--blue-dark);font-weight:400}
.intro{position:absolute;left:20px;top:458px;width:570px}
.intro p{font-size:9px;line-height:13.3px;color:#333;margin-top:10px}
.intro p+p{margin-top:27px}
.features-title{position:absolute;left:20px;top:622px}
.feature{position:absolute;width:278px;height:93px;border:1px solid #e0e0e0;background:#fff;box-shadow:0 1px 2px #eee}
.feature svg{position:absolute;left:12px;top:14px}
.feature h3{position:absolute;left:70px;top:15px;font-size:11px;font-weight:400;color:var(--blue)}
.feature p{position:absolute;left:70px;top:30px;width:198px;font-size:10px;line-height:15px;color:var(--blue)}

/* news */
.news{position:absolute;left:630px;top:462px;width:250px}
.news-item{margin-top:12px}
.news-item h4{font-weight:400;font-size:11px;color:var(--red)}
.news-item p{font-size:9.6px;line-height:15px;color:var(--blue);margin-top:4px}
.btn-read{display:inline-block;margin-top:6px;background:var(--blue);color:#fff;font-size:9.5px;padding:2px 10px;border-radius:2px}
.signup{position:absolute;left:620px;top:807px;width:260px;height:119px;background:linear-gradient(#e3eef8,#f4f8fb);border:1px solid #cfe0ee;border-radius:3px}
.signup h3{position:absolute;left:20px;top:12px}
.signup svg{position:absolute;left:167px;top:8px}
.signup .field{position:absolute;left:18px;top:42px;width:226px;height:25px;border:1px solid #c6d6e4;background:#fff;border-radius:2px;font-style:italic;color:var(--blue);font-size:10px;padding:5px 9px}
.btn-sub{position:absolute;left:150px;top:72px;width:90px;height:25px;background:var(--orange);color:#fff;font-size:14px;text-align:center;line-height:25px;border-radius:2px}

/* footer */
.site-footer{position:absolute;left:0;top:949px;width:910px;height:251px;background:var(--footer-bg)}
.site-footer h5{position:absolute;top:23px;font-size:13px;font-weight:400;color:#222}
.links{position:absolute;left:38px;top:52px;display:grid;grid-template-columns:115px 110px;row-gap:13px;font-size:11px;color:#444}
.vsep{position:absolute;top:40px;width:1px;height:126px;background:#d6d6d6}
.map{position:absolute;left:290px;top:48px;width:191px;height:124px;background:linear-gradient(135deg,#e9e6dc,#d7d4c6 55%,#c6d8b6);border:3px solid #fff;box-shadow:0 0 2px #999}
.form-field{position:absolute;left:533px;width:196px;height:20px;background:#fff;border:1px solid #dadada;border-radius:2px;font-size:9.5px;color:#777;padding:4px 9px}
.btn-send{position:absolute;left:665px;top:159px;width:64px;height:23px;background:#d3d3d3;border:1px solid #bbb;border-radius:2px;color:#555;font-size:13px;text-align:center;line-height:21px}
.foot-rule{position:absolute;left:20px;top:208px;width:850px;height:1px;background:#bbb}
.copyright{position:absolute;left:25px;top:224px;font-size:10px;color:#222}
</style>
</head>
<body>

<header class="site-header">
  <div class="brand"><span class="brand-dot"></span>Brelvo</div>
  <div class="login">username<input aria-label="username">Password<input aria-label="password" type="password"><a class="btn-login" href="#">log in</a><span class="welcome-user">Welcome ! Username</span></div>
  <nav class="main-nav">
    <a class="active" href="#">Main</a><a href="#">About Us</a><a href="#">Services</a><a href="#">Features</a><a href="#">News</a><a href="#">Contact</a>
  </nav>
</header>

<section class="hero">
  <h1>Interconnecting <span>Networks</span></h1>
  <h2>Networking Tittle line goes here</h2>
  <p>Static website is a simple way to get your message out to the public. Static website are cheaper and also it needs less maintenance too. It's the simplest, cheapest and also the basic thing the search engine picks it up very easily</p>
  <a class="btn-more" href="#">VIEW MORE &#9656;</a>
  <div class="dots"><i></i><i></i><i></i><i></i><i></i></div>
  <div class="hero-art" role="img" aria-label="Illustration of a blue globe linked to computers, laptops, phones and servers"></div>
</section>
<div class="hero-shadow"></div>

<section class="intro">
  <h2 class="section-title">Welcome to our Website Mainpage</h2>
  <p>Norvane Studio is a professional website design company dedicated to provide excellent services. We at Norvane think graphic design as a combination and collaboration of ideas and technology. Our Website Design team give an unforgettable impression on the customers and the clients. We can assure you that this is the best place for requirement of yours regarding website design solutions</p>
  <p>Norvane Studio provides you the Search Engine Optimization making your website search engine friendly. So that the website can achieve top position and ranking in the Internet searches and thereby increasing the scope for the website to be found by customers. We here modify the site to improve the ranking by using the keywords and contents.</p>
</section>

<h2 class="section-title abs features-title">Featured Overview</h2>

<svg width="0" height="0" style="position:absolute">
  <defs>
    <symbol id="icon-phone" viewBox="0 0 44 44"><rect x="1" y="1" width="42" height="42" rx="7" fill="#2b78c6" stroke="#9cc3e8" stroke-width="2"/><path d="M14 12c-3 3-2 9 4 15s12 7 15 4l-4-5-3 2c-2-1-6-5-7-7l2-3z" fill="#fff"/></symbol>
    <symbol id="icon-chat" viewBox="0 0 44 44"><path d="M3 4h38v26H18l-9 9v-9H3z" fill="#7cbd2e"/><rect x="10" y="12" width="24" height="2.5" fill="#fff"/><rect x="10" y="19" width="16" height="2.5" fill="#fff"/></symbol>
    <symbol id="icon-globe" viewBox="0 0 44 44"><circle cx="22" cy="22" r="20" fill="#1f5fb8"/><circle cx="16" cy="15" r="8" fill="#5a9ae0" opacity=".6"/></symbol>
  </defs>
</svg>

<article class="feature" style="left:21px;top:644px"><svg width="44" height="44"><use href="#icon-phone"/></svg><h3>TITTLE HERE</h3><p>When considering advanced web development project, finding the right answers to the hard questions is a challenge for any firm</p></article>
<article class="feature" style="left:300px;top:644px"><svg width="44" height="44"><use href="#icon-phone"/></svg><h3>TITTLE HERE</h3><p>When considering advanced web development project, finding the right answers to the hard questions is a challenge for any firm</p></article>
<article class="feature" style="left:21px;top:748px"><svg width="44" height="44"><use href="#icon-chat"/></svg><h3>TITTLE HERE</h3><p>When considering advanced web development project, finding the right answers to the hard questions is a challenge for any firm</p></article>
<article class="feature" style="left:300px;top:748px"><svg width="44" height="44"><use href="#icon-chat"/></svg><h3>TITTLE HERE</h3><p>When considering advanced web development project, finding the right answers to the hard questions is a challenge for any firm</p></article>
<article class="feature" style="left:21px;top:848px"><svg width="44" height="44"><use href="#icon-globe"/></svg><h3>TITTLE HERE</h3><p>When considering advanced web development project, finding the right answers to the hard questions is a challenge for any firm</p></article>
<article class="feature" style="left:300px;top:848px"><svg width="44" height="44"><use href="#icon-globe"/></svg><h3>TITTLE HERE</h3><p>When considering advanced web development project, finding the right answers to the hard questions is a challenge for any firm</p></article>

<aside class="news">
  <h2 class="section-title">News &amp; Events</h2>
  <div class="news-item"><h4>Headline goes here</h4><p>E-Commerce is a major progress in technology that has changed the way in which the customers</p><a class="btn-read" href="#">READ MORE</a></div>
  <div class="news-item"><h4>Headline goes here</h4><p>E-Commerce is a major progress in technology that has changed the way in which the customers</p><a class="btn-read" href="#">READ MORE</a></div>
  <div class="news-item"><h4>Headline goes here</h4><p>We like challenges and do complete these challenge</p><a class="btn-read" href="#">READ MORE</a></div>
  <div class="news-item"><h4>Headline goes here</h4><p>E-Commerce is a major progress in technology</p><a class="btn-read" href="#">READ MORE</a></div>
</aside>

<section class="signup">
  <h3 class="section-title">Sign Up Newsletters</h3>
  <svg width="32" height="28" viewBox="0 0 32 28"><rect x="2" y="8" width="28" height="18" fill="#f3c640" stroke="#d9a820"/><path d="M2 8l14 10 14-10" fill="none" stroke="#d9a820"/><circle cx="16" cy="8" r="6" fill="#f59a2a"/></svg>
  <div class="field">your email address</div>
  <a class="btn-sub" href="#">Subscribe</a>
</section>

<footer class="site-footer">
  <h5 style="left:38px">Quick Links</h5>
  <nav class="links">
    <a href="#">Main Page</a><a href="#">News &amp; Events</a>
    <a href="#">Services</a><a href="#">Testimonials</a>
    <a href="#">About Us</a><a href="#">Blog</a>
    <a href="#">Features</a><a href="#">Contact Us</a>
    <a href="#">Newsletters</a>
  </nav>
  <div class="vsep" style="left:260px"></div>
  <h5 style="left:289px">Contact Map</h5>
  <div class="map" role="img" aria-label="Street map showing the office location"></div>
  <div class="vsep" style="left:510px"></div>
  <h5 style="left:535px">Contact Form</h5>
  <div class="form-field" style="top:52px">type your name</div>
  <div class="form-field" style="top:80px">type your phone no.</div>
  <div class="form-field" style="top:106px">type your email address</div>
  <div class="form-field" style="top:134px">type your city/Zone</div>
  <a class="btn-send" href="#">SEND</a>
  <div class="foot-rule"></div>
  <p class="copyright">© 2012 Company Name &nbsp;|&nbsp; All right reserved</p>
</footer>

</body>
</html>
```